Personal Business card and maybe logo or graphic?

I would like a card to give out like you would a business card, however I am not promoting a business, it is just for my personal details.

I have no brand and no logo to worry about.

I would like some images or a logo of some kind or a graphic so the card has some excitement about it.

I am happy if you wish to create a logo/graphic that represents my name, I have seen someone with just their initials as a graphic so for me PH, however I am happy for you to create anything you wish, it does not have to relate to me just make the card look fun and still professional.

Please use the details

Peter Hadley

Ashcombe Lodge
9 The Mews
Fern Close
Bournemouth
Dorset
BH4 2QT

+44 (0)7812 604258
peter@hadleypost.example
linkedin.example/in/hadleypeter

looking for a mix between fun, fresh , young whilst being professional

I am new to this and am looking for you to guide me through the process please ask questions and ideas

I am just tidying up my brief as I am starting to understand more. hope it has not confused anyone
Updates

Reason: I have not had time to review or comment due to personal issues sorry

Hi,

to help would you be so kind as to use these sample details on the card

I am uk based and a few designs have us details which look different

Peter Hadley

Ashcombe lodge

9 The Mews

Fern Close

Bournemouth

Dorset

BH4 2QT

+44 (0)7812 604258

peter@hadleypost.example

many thanks hope that is ok and not too much trouble!

regards

Pim

My are of expertise is IT management / IT Consultancy, incase you wish to incorporate any graphics

My job was that of CIO (Chief Information Officer) or another term is Head of IT

just advising incase this gives any assistance as one designer has asked s may be useful to others

thanks                                   

just thought I have had a look and the UK size for a business card seems to be as per below

I thought I would mention as I guess the US size may be different and other countries too

I found these sizes on Cardforge but guess most companies will be similar

that said maybe you can advise me

I have no idea what cardforge is like so not sure where to get cards made, will figure that out later I guess but I assume dimensions are important for the design

thanks

 

Document Trim Size    

            Horizontal        

        85 x 55 mm           

1004 x 650 pixels           

            Vertical        

        55 x 85 mm           

650 x 1004 pixels           

        Full Bleed Size    

            Horizontal        

        88 x 58 mm           

1039 x 685 pixels           

            Vertical        

        58 x 88 mm           

685 x 1039 pixels           

 many thanks

Target Market(s)

Professional and personal contacts

Industry/Entity Type

Business

```html
<!DOCTYPE html>
<html lang="en">
<head>
<meta charset="utf-8">
<title>Peter Hadley – Business Card</title>
<link href="https://fonts.googleapis.com/css2?family=Gelasio:wght@400;700&display=swap" rel="stylesheet">
<style>
  :root {
    --page-bg: #e9e6e1;
    --card-white: #ffffff;
    --card-blue: #00aeef;
    --brand-red: #e8212b;
    --ink: #111111;
    --shadow: rgba(0, 0, 0, 0.18);
  }
  * { box-sizing: border-box; margin: 0; padding: 0; }
  html, body {
    width: 1200px;
    height: 1200px;
    overflow: hidden;
    background: var(--page-bg);
  }
  .canvas {
    width: 1200px;
    height: 1200px;
    display: flex;
    flex-direction: column;
    align-items: center;
    justify-content: center;
    gap: 44px;
    font-family: "Gelasio", Georgia, serif;
  }
  .card {
    position: relative;
    width: 820px;
    height: 530px;
    border-radius: 40px;
    overflow: hidden;
    box-shadow: 0 8px 24px var(--shadow);
  }

  /* Front */
  .card--front {
    background: var(--card-white);
    display: flex;
    align-items: center;
  }
  .front__mark {
    width: 400px;
    display: flex;
    justify-content: center;
    align-items: center;
  }
  .monogram {
    font-family: "Gelasio", Georgia, serif;
    font-weight: 700;
    color: var(--brand-red);
    font-size: 190px;
    line-height: 1;
    letter-spacing: 4px;
  }
  .front__divider {
    width: 6px;
    height: 380px;
    background: var(--ink);
  }
  .front__identity {
    padding-left: 26px;
  }
  .identity__name {
    font-size: 62px;
    font-weight: 400;
    color: var(--ink);
    line-height: 1.1;
    letter-spacing: -1px;
  }
  .identity__role {
    margin-top: 10px;
    font-size: 28px;
    color: var(--brand-red);
    letter-spacing: -0.3px;
  }

  /* Back */
  .card--back {
    background: var(--card-blue);
  }
  .back__mark {
    position: absolute;
    top: 22px;
    left: 0;
    right: 0;
    text-align: center;
  }
  .back__mark .monogram {
    font-size: 120px;
  }
  .back__details {
    position: absolute;
    top: 180px;
    left: 0;
    right: 0;
    height: 250px;
    background: var(--card-white);
    display: flex;
    padding: 38px 0 0 78px;
    gap: 58px;
  }
  .address {
    font-style: normal;
    font-size: 34px;
    line-height: 1.1;
    color: var(--ink);
  }
  .contact {
    color: var(--ink);
  }
  .contact__county {
    font-size: 34px;
    font-weight: 700;
    letter-spacing: 4px;
    line-height: 1;
  }
  .contact__postcode {
    font-size: 26px;
    font-weight: 700;
    letter-spacing: 6px;
    margin-top: 4px;
  }
  .contact__phone {
    font-size: 28px;
    margin-top: 12px;
  }
  .contact__email {
    font-size: 23px;
    margin-top: 6px;
  }
  .back__link {
    position: absolute;
    top: 444px;
    left: 0;
    right: 0;
    text-align: center;
    font-size: 30px;
    color: var(--brand-red);
    letter-spacing: 0.5px;
  }
</style>
</head>
<body>
<main class="canvas">
  <section class="card card--front" aria-label="Card front">
    <div class="front__mark">
      <span class="monogram">PH</span>
    </div>
    <div class="front__divider"></div>
    <div class="front__identity">
      <h1 class="identity__name">Peter Hadley</h1>
      <p class="identity__role">Chief Information Officer</p>
    </div>
  </section>

  <section class="card card--back" aria-label="Card back">
    <div class="back__mark">
      <span class="monogram">PH</span>
    </div>
    <div class="back__details">
      <address class="address">
        Ashcombe lodge<br>
        9 The Mews<br>
        Fern Close<br>
        Bournemouth
      </address>
      <div class="contact">
        <p class="contact__county">Dorset</p>
        <p class="contact__postcode">BH4 2QT</p>
        <p class="contact__phone">+44 (0)7812 604258</p>
        <p class="contact__email">peter@hadleypost.example</p>
      </div>
    </div>
    <p class="back__link">linkedin.example/in/hadleypeter</p>
  </section>
</main>
</body>
</html>
```